Clean bold and classy business card front and back
Kwr can be the logo
My name Trent Holloman as owner
Phone email and address
Owner Trent Holloman
Phone 8505550147
Email ridgelineinsulate@mailnest.example
Address170 frank pais rd Havana fl 32399

Industry/Entity Type

Business

Contact Information for Business Card

Owner Trent Holloman
Phone 8505550147

Requirements
Must have
• Keystone wall render under Kwr logo
Nice to have
• Bold and clean. Maybe use Kwr as logo and name under it. Have logo on one side and info on the other side with logo also
• Put a pic up. It doesn't have to be that but something that can be used
• Try some fancy fonts also

```html
<!DOCTYPE html>
<html lang="en">
<head>
<meta charset="utf-8">
<title>Kwr – Business Card</title>
<link rel="stylesheet" href="https://fonts.googleapis.com/css2?family=Open+Sans:wght@400;600;700&display=swap">
<style>
  :root {
    --stage: #e9e9ea;
    --card: #ffffff;
    --charcoal: #4a4a4d;
    --charcoal-deep: #2e2e31;
    --ink: #1d1d1f;
    --brand-blue: #1f8fe0;
    --sky-blue: #36b4f0;
    --text-light: #ffffff;
  }
  * { box-sizing: border-box; margin: 0; padding: 0; }
  html, body { width: 1200px; height: 913px; overflow: hidden; }
  body {
    background: var(--stage);
    font-family: "Open Sans", Arial, sans-serif;
    position: relative;
  }
  .card {
    position: absolute;
    top: 313px;
    width: 500px;
    height: 286px;
    border-radius: 16px;
    background: var(--card);
    overflow: hidden;
    box-shadow: 0 6px 18px rgba(0,0,0,0.18);
  }
  .card--front { left: 70px; }
  .card--back { left: 630px; }

  .front-wave { position: absolute; inset: 0; width: 100%; height: 100%; }

  .brand {
    position: absolute;
    right: 34px;
    top: 20px;
    text-align: left;
  }
  .brand__name {
    font-weight: 700;
    font-size: 52px;
    line-height: 1;
    color: var(--charcoal);
    letter-spacing: 1px;
  }
  .brand__tagline {
    font-weight: 600;
    font-size: 13px;
    line-height: 16px;
    color: var(--brand-blue);
    margin-top: 4px;
    letter-spacing: 0.3px;
  }

  .contact {
    position: absolute;
    left: 30px;
    top: 170px;
    color: var(--text-light);
  }
  .contact__name { font-weight: 700; font-size: 22px; line-height: 1.1; }
  .contact__role { font-size: 13px; line-height: 18px; color: var(--sky-blue); margin-bottom: 6px; }
  .contact__list { list-style: none; }
  .contact__item {
    display: flex;
    align-items: center;
    gap: 8px;
    font-size: 12.5px;
    line-height: 18px;
  }
  .contact__icon { width: 11px; height: 11px; flex: none; }

  .back-mark {
    position: absolute;
    left: 50%;
    top: 50%;
    width: 180px;
    height: 180px;
    transform: translate(-50%, -50%);
    border: 5px solid var(--sky-blue);
    border-radius: 50%;
    display: flex;
    align-items: center;
    justify-content: center;
  }
  .back-mark__name {
    font-weight: 700;
    font-size: 58px;
    color: var(--charcoal);
    letter-spacing: 1px;
  }
</style>
</head>
<body>

  <section class="card card--front" aria-label="Business card front">
    <svg class="front-wave" viewBox="0 0 500 286" preserveAspectRatio="none" aria-hidden="true">
      <defs>
        <linearGradient id="panelShade" x1="0" y1="0" x2="1" y2="1">
          <stop offset="0" stop-color="#5a5a5e"/>
          <stop offset="1" stop-color="#35353a"/>
        </linearGradient>
      </defs>
      <path d="M0,126 C120,116 210,198 330,166 S450,110 500,112 L500,286 L0,286 Z" fill="var(--ink)"/>
      <path d="M0,134 C120,126 210,208 330,176 S450,120 500,122 L500,286 L0,286 Z" fill="var(--brand-blue)"/>
      <path d="M0,140 C120,134 210,216 330,184 S450,128 500,130 L500,286 L0,286 Z" fill="url(#panelShade)"/>
      <path d="M0,214 L6,214 Q12,214 12,220 L12,286 L0,286 Z" fill="var(--brand-blue)"/>
    </svg>

    <div class="brand">
      <div class="brand__name">Kwr</div>
      <div class="brand__tagline">Keystone wall render</div>
    </div>

    <div class="contact">
      <div class="contact__name">Trent Holloman</div>
      <div class="contact__role">Owner</div>
      <ul class="contact__list">
        <li class="contact__item">
          <svg class="contact__icon" viewBox="0 0 12 12" aria-hidden="true"><path d="M2.5 0.8 L4.6 3.2 L3.5 4.6 Q4.6 7 7.3 8.4 L8.7 7.3 L11.2 9.4 L10 11.2 Q5.5 11 2.4 7.6 Q0.6 5 0.8 2 Z" fill="var(--sky-blue)"/></svg>
          850 555-0147
        </li>
        <li class="contact__item">
          <svg class="contact__icon" viewBox="0 0 12 12" aria-hidden="true"><rect x="0.7" y="2.2" width="10.6" height="7.6" rx="1" fill="none" stroke="var(--sky-blue)" stroke-width="1.3"/><path d="M1 2.6 L6 6.6 L11 2.6" fill="none" stroke="var(--sky-blue)" stroke-width="1.3"/></svg>
          ridgelineinsulate@mailnest.example
        </li>
        <li class="contact__item">
          <svg class="contact__icon" viewBox="0 0 12 12" aria-hidden="true"><path d="M6 0.5 A4 4 0 0 1 10 4.5 C10 7.5 6 11.5 6 11.5 C6 11.5 2 7.5 2 4.5 A4 4 0 0 1 6 0.5 Z" fill="var(--sky-blue)"/><circle cx="6" cy="4.5" r="1.5" fill="var(--charcoal-deep)"/></svg>
          428 dunmore ct Havana fl 32399
        </li>
      </ul>
    </div>
  </section>

  <section class="card card--back" aria-label="Business card back">
    <div class="back-mark">
      <span class="back-mark__name">Kwr</span>
    </div>
  </section>

</body>
</html>
```